STAND OUT BUSINESS CARD REQUIRED

I would like a business card that is going to be different and stand out!

Target Market(s)

Residential market, adults from 28yrs on

Industry/Entity Type

Electrician

Requirements
Must have
• Business name
• my name
• phone number
• email
• web address
• license no.
• abn
• fax no
• logo
Nice to have
• Extra info:
• FREE quotes
• Fixed pricing
• On time guarantee
• Life time labour Guarantee

```html
<!DOCTYPE html>
<html lang="en">
<head>
<meta charset="utf-8">
<title>Bright Spark Pty Ltd – Business Card</title>
<link rel="stylesheet" href="https://fonts.googleapis.com/css2?family=Open+Sans:wght@400;700&family=Nunito:wght@800;900&display=swap">
<style>
  :root {
    --backdrop: #e8e4de;
    --card: #232323;
    --orange: #f07c1a;
    --white: #ffffff;
    --shadow: rgba(0, 0, 0, 0.35);
    --art-a: #6aa84f;
    --art-b: #d9482b;
  }
  html, body {
    margin: 0;
    padding: 0;
    overflow: hidden;
  }
  .canvas {
    position: relative;
    width: 1200px;
    height: 831px;
    background: var(--backdrop);
    overflow: hidden;
  }
  .card {
    position: absolute;
    width: 620px;
    height: 354px;
    background: var(--card);
    box-shadow: 0 10px 24px var(--shadow);
    overflow: hidden;
  }
  .card--front { left: 60px; top: 60px; }
  .card--back { left: 520px; top: 420px; }

  .holder {
    position: absolute;
    left: 30px;
    top: 48px;
    font-family: "Open Sans", sans-serif;
    color: var(--white);
  }
  .holder__name {
    margin: 0;
    font-size: 29px;
    font-weight: 700;
    letter-spacing: 0.5px;
    color: var(--orange);
    line-height: 1;
  }
  .holder__role {
    margin: 6px 0 0;
    font-size: 16px;
  }
  .contact {
    position: absolute;
    left: 30px;
    font-family: "Open Sans", sans-serif;
    color: var(--white);
    font-size: 16px;
    border-collapse: collapse;
  }
  .contact th {
    text-align: left;
    font-weight: 700;
    padding: 0 40px 1px 0;
  }
  .contact td { padding: 0 0 1px; }
  .contact--phone { top: 155px; }
  .contact--online { top: 244px; }

  .brand {
    position: absolute;
    left: 370px;
    top: 118px;
    width: 220px;
    text-align: center;
  }
  .brand__art {
    display: block;
    margin: 0 auto;
  }
  .brand__name {
    margin: 8px 0 0;
    font-family: "Nunito", sans-serif;
    font-weight: 900;
    font-size: 24px;
    line-height: 1.05;
    color: var(--orange);
    text-transform: uppercase;
  }

  .promises {
    position: absolute;
    left: 50%;
    top: 50%;
    transform: translate(-50%, -50%) rotate(-22deg);
    font-family: "Nunito", sans-serif;
    font-weight: 900;
    text-transform: uppercase;
    text-align: center;
    white-space: nowrap;
    line-height: 1.1;
  }
  .promises__line { margin: 0; }
  .promises__line--small { font-size: 30px; }
  .promises__line--large { font-size: 46px; color: var(--orange); }
  .is-orange { color: var(--orange); }
  .is-white { color: var(--white); }
</style>
</head>
<body>
<main class="canvas">
  <section class="card card--front" aria-label="Business card front">
    <header class="holder">
      <h1 class="holder__name">MARCUS REID HALE</h1>
      <p class="holder__role">Chief Executive Director</p>
    </header>

    <table class="contact contact--phone">
      <tr><th>phone</th><td>+03 7100 4821</td></tr>
      <tr><th>mobile</th><td>+03 5200 3176</td></tr>
    </table>

    <table class="contact contact--online">
      <tr><th>email</th><td>mrh@brightmail.com</td></tr>
      <tr><th>web</th><td>brightsparkpower.com</td></tr>
      <tr><th>license #</th><td>4416730</td></tr>
    </table>

    <div class="brand">
      <svg class="brand__art" width="150" height="110" viewBox="0 0 150 110" role="img" aria-label="Mascot illustration: caped electrician hero holding up a light bulb">
        <defs>
          <linearGradient id="mascot-tone" x1="0" y1="0" x2="1" y2="1">
            <stop offset="0" stop-color="var(--art-a)"/>
            <stop offset="1" stop-color="var(--art-b)"/>
          </linearGradient>
        </defs>
        <rect x="0" y="0" width="150" height="110" rx="14" fill="url(#mascot-tone)" opacity="0.85"/>
      </svg>
      <p class="brand__name">Bright Spark<br>Pty Ltd</p>
    </div>
  </section>

  <section class="card card--back" aria-label="Business card back">
    <div class="promises">
      <p class="promises__line promises__line--small"><span class="is-orange">Free Quotes</span> <span class="is-white">• Fixed Pricing</span></p>
      <p class="promises__line promises__line--large">On Time Guarantee</p>
      <p class="promises__line promises__line--small is-white">Lifetime Labour Guarantee</p>
    </div>
  </section>
</main>
</body>
</html>
```